Business Card Design

We would like a business card that utilizes our current logo and keeps with the same feel - elegant and organic. Our farm isn't about mass production, it's about excellence, education, beautiful events and flowers - people, culture, and community.

Target Market(s)

Patrons to our farm who are interested in weddings, events, or our flowers and vegetables.

Contact Information for Business Card

Name, address, cell email (Danielle Hoskins, 2716 Wrenfield Rd, Brookvale, CO 80541, cell 30.412.6638, email danielle@wrenfieldacres.com)

```html
<!DOCTYPE html>
<html lang="en">
<head>
<meta charset="utf-8">
<title>Wrenfield Acres — Business Card</title>
<link href="https://fonts.googleapis.com/css2?family=Open+Sans:wght@400;600&display=swap" rel="stylesheet">
<style>
  :root {
    --stage: #1d2120;
    --sage: #86ab9a;
    --sage-deep: #6f9483;
    --paper: #fbfaf7;
    --ink-green: #8aa895;
    --ink-gold: #c9a06e;
    --ink-grey: #8a8d8b;
    --rule: #d8d2c4;
    --white: #ffffff;
  }
  * { box-sizing: border-box; margin: 0; padding: 0; }
  html, body { width: 1200px; height: 866px; overflow: hidden; }
  body {
    background: var(--stage);
    font-family: "Open Sans", Arial, sans-serif;
    display: flex;
    align-items: center;
    justify-content: center;
    gap: 40px;
  }
  .card {
    width: 540px;
    height: 309px;
    border-radius: 3px;
    position: relative;
    overflow: hidden;
  }
  .card-front {
    background: linear-gradient(135deg, var(--sage-deep), var(--sage));
    display: flex;
    align-items: center;
    justify-content: center;
  }
  .brand-name {
    font-family: "Open Sans", Arial, sans-serif;
    font-weight: 400;
    letter-spacing: 0.08em;
    white-space: nowrap;
  }
  .card-front .brand-name {
    color: var(--white);
    font-size: 38px;
  }
  .card-back { background: var(--paper); }
  .card-back .brand-name {
    position: absolute;
    top: 58px;
    right: 44px;
    color: var(--ink-green);
    font-size: 26px;
  }
  .divider {
    position: absolute;
    left: 190px;
    right: 44px;
    top: 150px;
    height: 1px;
    background: var(--rule);
  }
  .address {
    position: absolute;
    right: 44px;
    top: 168px;
    text-align: right;
    color: var(--ink-grey);
    font-size: 13px;
    line-height: 1.45;
  }
  .person {
    position: absolute;
    left: 36px;
    top: 140px;
  }
  .person-name {
    color: var(--ink-green);
    font-weight: 600;
    font-size: 15px;
    letter-spacing: 0.02em;
    text-transform: uppercase;
  }
  .person-title {
    color: var(--ink-gold);
    font-size: 13px;
    margin-top: 1px;
  }
  .contact-list {
    list-style: none;
    margin-top: 16px;
    color: var(--ink-grey);
    font-size: 12.5px;
    line-height: 1.6;
  }
  .contact-list li { display: flex; align-items: center; gap: 8px; }
  .contact-list svg { width: 10px; height: 10px; flex: none; }
</style>
</head>
<body>
  <section class="card card-front" aria-label="Card front">
    <span class="brand-name">Wrenfield Acres</span>
  </section>

  <section class="card card-back" aria-label="Card back">
    <span class="brand-name">Wrenfield Acres</span>
    <div class="divider"></div>
    <p class="address">2716 Wrenfield Rd,<br>Brookvale, CO 80541</p>
    <div class="person">
      <p class="person-name">Danielle Hoskins</p>
      <p class="person-title">Founder &amp; CEO</p>
      <ul class="contact-list">
        <li>
          <svg viewBox="0 0 10 10" aria-hidden="true"><rect x="2" y="0.5" width="6" height="9" rx="1" fill="none" stroke="#8a8d8b"/></svg>
          30.412.6638
        </li>
        <li>
          <svg viewBox="0 0 10 10" aria-hidden="true"><rect x="0.5" y="2" width="9" height="6.5" fill="none" stroke="#8a8d8b"/><path d="M0.5 2 L5 6 L9.5 2" fill="none" stroke="#8a8d8b"/></svg>
          danielle@wrenfieldacres.com
        </li>
        <li>
          <svg viewBox="0 0 10 10" aria-hidden="true"><circle cx="5" cy="5" r="4.5" fill="none" stroke="#8a8d8b"/><path d="M0.5 5 H9.5 M5 0.5 C2.5 3 2.5 7 5 9.5 M5 0.5 C7.5 3 7.5 7 5 9.5" fill="none" stroke="#8a8d8b" stroke-width="0.8"/></svg>
          www.wrenfieldacres.com
        </li>
      </ul>
    </div>
  </section>
</body>
</html>
```